catering postcard

We need a postcard that lets offices know that we cater and can deliver our delicious food to their office/meeting/event.

We are a mom and pop, super busy, well-loved Italian restaurant.
(check us out at marcostrattoriaweb.com)

The final design should communicate delicious food, brought to your place of work. It arrives on time and is hot and ready to be devoured.

We'd like to see bright colors and a huge impact on our lunch time catering sales.

Industry/Entity Type

Catering

```html
<!DOCTYPE html>
<html lang="en">
<head>
<meta charset="utf-8">
<title>Marco's Trattoria – Catering Postcard</title>
<link rel="stylesheet" href="https://fonts.googleapis.com/css2?family=Lobster&family=Roboto:wght@400&display=swap">
<style>
  :root {
    --page-bg: #ececec;
    --card-white: #ffffff;
    --brand-red: #a8190e;
    --brand-green: #2f8f2a;
    --script-green: #3a9a2e;
    --phone-red: #e0141c;
    --gold: #f2c46a;
    --ink-black: #060606;
  }
  * { margin: 0; padding: 0; box-sizing: border-box; }
  html, body { width: 1200px; height: 841px; overflow: hidden; }
  body { background: var(--page-bg); position: relative; font-family: "Roboto", Arial, sans-serif; }

  .script { font-family: "Lobster", cursive; font-weight: 400; }

  /* Back of card */
  .card-back {
    position: absolute; left: 34px; top: 36px; width: 716px; height: 551px;
    background: var(--card-white);
  }
  .back-photo {
    position: absolute; left: 0; top: 0; width: 356px; height: 469px;
    background: linear-gradient(180deg, var(--ink-black) 0%, var(--ink-black) 42%, #3a2417 60%, #d9c9b0 78%, #f1ece4 100%);
  }
  .back-message {
    position: absolute; left: 0; top: 44px; width: 356px; text-align: center;
  }
  .back-message .invite { color: var(--script-green); font-size: 31px; line-height: 40px; transform: rotate(-3deg); }
  .back-message .phone { color: var(--phone-red); font-size: 33px; line-height: 44px; margin-top: 6px; transform: rotate(-3deg); }

  /* Front of card */
  .card-front {
    position: absolute; left: 435px; top: 245px; width: 716px; height: 552px;
    background: var(--card-white);
  }
  .brand-block {
    position: absolute; left: 0; top: 0; width: 322px; height: 180px;
    display: flex; align-items: center; justify-content: center; gap: 12px;
  }
  .brand-mark { width: 18px; height: 18px; border-radius: 50%; background: var(--brand-green); }
  .brand-name { color: var(--brand-green); font-size: 36px; }
  .promise {
    position: absolute; left: 322px; top: 0; width: 394px; height: 180px;
    background: var(--brand-red); color: var(--gold);
    display: flex; align-items: center; justify-content: center; text-align: center;
    font-size: 24px; line-height: 37px; padding-top: 4px;
  }
  .divider { position: absolute; left: 0; top: 180px; width: 716px; height: 6px; background: var(--brand-green); }

  .photo { position: absolute; }
  .photo-peppers { left: 0; top: 186px; width: 528px; height: 178px;
    background: linear-gradient(90deg, #2f3a1c 0%, #6a7d2e 35%, #8aa13c 55%, #c9c2a8 75%, #3d3a20 100%); }
  .photo-cake { left: 528px; top: 186px; width: 188px; height: 178px;
    background: linear-gradient(160deg, #cfd3cf 0%, #b98a54 45%, #efe8dc 75%, #bdb7ad 100%); }
  .photo-meatballs { left: 0; top: 364px; width: 213px; height: 188px;
    background: linear-gradient(180deg, #4a2a1c 0%, #c3412a 40%, #e7d8c6 70%, #3f6a25 90%); }
  .photo-sauce { left: 503px; top: 364px; width: 213px; height: 188px;
    background: linear-gradient(200deg, #4a3a2c 0%, #8b5a3e 40%, #b9321d 70%, #e8dccd 100%); }

  .order-panel {
    position: absolute; left: 213px; top: 364px; width: 290px; height: 188px;
    background: var(--brand-red); color: var(--card-white); padding: 12px 0 0 30px;
  }
  .order-panel .cta { font-size: 30px; line-height: 40px; }
  .order-panel .phone { font-size: 33px; line-height: 42px; }
  .address { display: flex; align-items: center; gap: 12px; margin-top: 14px; margin-left: -5px; }
  .address svg { width: 38px; height: 38px; flex: none; }
  .address p { font-size: 16.5px; line-height: 22px; }
</style>
</head>
<body>

  <section class="card-back">
    <div class="back-photo" role="img" aria-label="Photo of a chocolate-dipped cannoli with chocolate chip ricotta filling on a white plate"></div>
    <div class="back-message script">
      <p class="invite">For Delicious Meals,<br>Please Call</p>
      <p class="phone">(205) 555-0148</p>
    </div>
  </section>

  <section class="card-front">
    <div class="brand-block">
      <span class="brand-mark"></span>
      <span class="brand-name script">Marco's Trattoria</span>
    </div>
    <div class="promise script">
      <p>Delicious Food at<br>Your Workplace On Time<br>and is Hot and<br>Ready to be Devoured.</p>
    </div>
    <div class="divider"></div>

    <div class="photo photo-peppers" role="img" aria-label="Photo of stuffed green peppers topped with tomato sauce and grated cheese"></div>
    <div class="photo photo-cake" role="img" aria-label="Photo of a slice of layered carrot cake with cream frosting"></div>
    <div class="photo photo-meatballs" role="img" aria-label="Photo of meatballs in tomato sauce with grated cheese and a basil leaf"></div>

    <div class="order-panel">
      <p class="cta script">For Order Call</p>
      <p class="phone script">(205) 555-0148</p>
      <div class="address">
        <svg viewBox="0 0 38 38" aria-hidden="true">
          <circle cx="19" cy="19" r="19" fill="#ffffff"/>
          <path d="M19 8c-4.4 0-7.5 3.2-7.5 7.3 0 5.2 7.5 14.2 7.5 14.2s7.5-9 7.5-14.2C26.5 11.2 23.4 8 19 8z" fill="#a8190e"/>
          <circle cx="19" cy="15.3" r="2.8" fill="#ffffff"/>
        </svg>
        <p>48 Brookline Park Drive<br>Alabaster, Alabama 35007</p>
      </div>
    </div>

    <div class="photo photo-sauce" role="img" aria-label="Photo of a ladle pouring meat sauce onto a plate of pasta"></div>
  </section>

</body>
</html>
```